AMAZING FLYERS, POSTCARDS, AND MARKETING!!!! - Northbeam Shingle & Gutter Works, LLC

This project will be for Northbeam Shingle & Gutter Works, LLC. The flyers and postcards will be used to saturate the Alaska market with our services, and get our name and logo out there for people to remember. We plan to send the flyers and postcards out in a broad scale (both door to door and mail out). We want to send out flyers to realty and property management businesses to introduce our roofing company, and to advertise our services. We would also like to have another version, or the ability to edit the text of the final product to send out the same materials to residential clients (homeowners) by just changing the text slightly to better fit that market.
We have a logo, but need something put together that we can tri-fold and mail out to potential clients. We are planning to do some postcards as well. We would like the option to mail them or bring them to people in person.
We are a locally owned roofing and repair company in Alaska. We would like something professional that will capture their attention and show the potential of working with our company. I included some detailed information about our company and some pictures below of our work trailer and a before/after on a recent project. I also attached our logo files. Please go through the attached data and let us know what you come up with to stir up the marketing aspect of our company. Thank you for your time and consideration.
Updates

Project Deadline Extended
Reason: Allowing additional time for designers to submit/resubmit their flyer/postcard ideas based on inquiries and feedback.

Target Market(s)

1.) Homeowners are the first target market.
2.)Realtors and Property Management companies are the second market

Industry/Entity Type

Marketing

Contact Information for Business Card

Include the logo and contact information for our company. These business cards will be for the Owner, Marcus Velloway, II.
There is also a Co-Owner, Trina Velloway, so we will need the ability to print business cards for each owner. Need to be able to change the title/name and phone number for Trina's contact information please. Contact information, license #, and logo information on one side of the card. Please tell the potential client a little about us on the back of the card by utilizing the attached information.

Requirements
Must have
• Pertinent information about our company and listed in the company information attachment. Attention getting details and design work. Professional in appearance and unique to our company to set us above the general advertisers in this industry.
Nice to have
• Something that sets our flyers apart from the ones people get every day. We want to rise above normal with our advertising.
Should not have
• Nothing plain and boring.

```html
<!DOCTYPE html>
<html lang="en">
<head>
<meta charset="utf-8">
<title>Northbeam Shingle &amp; Gutter Works – Tri-fold Brochure</title>
<link rel="stylesheet" href="https://fonts.googleapis.com/css2?family=Jost:wght@400;500;700&family=Oswald:wght@400;500&display=swap">
<style>
:root{
  --ink:#0d0d0d;
  --paper:#ffffff;
  --stage:#e4e4e4;
  --mid:#8a8a8a;
  --soft:#cfcfcf;
  --text-light:#f2f2f2;
}
*{box-sizing:border-box;margin:0;padding:0}
html,body{width:1200px;height:675px;overflow:hidden;background:var(--stage)}
body{font-family:"Jost",sans-serif;position:relative}
.sheet{position:absolute;top:116px;width:570px;height:442px;overflow:hidden;background:var(--paper);box-shadow:0 4px 14px rgba(0,0,0,.25)}
.sheet--inside{left:20px}
.sheet--outside{left:610px}
.sheet svg.art{position:absolute;inset:0;width:570px;height:442px}
.block{position:absolute}
.heading-strip{position:absolute;background:var(--paper);color:var(--ink);font-family:"Jost",sans-serif;font-weight:700;font-size:9px;letter-spacing:.2px;padding:3px 8px;white-space:nowrap;line-height:12px;box-shadow:2px 2px 0 var(--mid)}
.heading-plain{font-family:"Jost",sans-serif;font-weight:700;font-size:10px;color:var(--ink);margin-bottom:5px;white-space:nowrap}
.body-copy{font-size:6.6px;line-height:1.42;text-align:justify}
.body-copy p{margin-bottom:4px}
.body-copy--light{color:var(--text-light)}
.body-copy--dark{color:var(--ink)}
.brand-name{font-family:"Jost",sans-serif;font-weight:700;text-align:center;line-height:1.15;text-transform:uppercase}
.brand-name--dark{color:var(--ink)}
.brand-name--light{color:var(--paper)}
.brand-mark{display:inline-block;margin-right:4px}
.brand-name--dark .brand-mark{background:var(--ink)}
.brand-name--light .brand-mark{background:var(--paper)}
.pill{display:inline-block;background:var(--ink);color:var(--paper);font-family:"Oswald",sans-serif;font-weight:400;border-radius:10px;border:1px solid var(--mid);white-space:nowrap}
.contact-list{list-style:none;color:var(--ink);font-weight:500;display:flex;flex-direction:column;gap:2px;text-align:left;font-size:8px}
.contact-list li{display:flex;align-items:center;gap:4px;white-space:nowrap}
.contact-list svg{width:7px;height:7px;flex:none}
.cover-title{color:var(--paper);font-family:"Jost",sans-serif;font-weight:400;text-transform:uppercase;line-height:1.05;text-align:center}
.cover-title strong{font-weight:700}
.cover-tagline{color:var(--ink);font-weight:500;text-transform:uppercase;letter-spacing:.5px;text-align:center;white-space:nowrap;height:14px;line-height:14px;transform:rotate(11.9deg);transform-origin:center}
</style>
</head>
<body>

<section class="sheet sheet--inside" aria-label="Brochure inside spread">
  <svg class="art" viewBox="0 0 570 442">
    <defs>
      <linearGradient id="inGrey" x1="0" y1="0" x2="0" y2="1">
        <stop offset="0" stop-color="#ffffff"/><stop offset="1" stop-color="#a9a9a9"/>
      </linearGradient>
      <linearGradient id="roofPhoto" x1="0" y1="0" x2="0" y2="1">
        <stop offset="0" stop-color="#111"/><stop offset=".35" stop-color="#555"/><stop offset="1" stop-color="#9a9a9a"/>
      </linearGradient>
      <linearGradient id="housePhoto" x1="0" y1="0" x2="0" y2="1">
        <stop offset="0" stop-color="#b9c3c9"/><stop offset=".55" stop-color="#7d8584"/><stop offset="1" stop-color="#5f7a48"/>
      </linearGradient>
      <linearGradient id="hexPhoto" x1="0" y1="0" x2="0" y2="1">
        <stop offset="0" stop-color="#7a8a6a"/><stop offset=".3" stop-color="#4a4a4a"/><stop offset="1" stop-color="#6d6d6d"/>
      </linearGradient>
    </defs>
    <rect x="0" y="0" width="190" height="442" fill="#0d0d0d"/>
    <rect x="0" y="300" width="190" height="142" fill="url(#roofPhoto)" role="img" aria-label="Photo of a finished shingle roof with vent pipes"/>
    <rect x="190" y="0" width="380" height="442" fill="url(#inGrey)"/>
    <polygon points="190,150 380,200 190,250" fill="#d8d8d8"/>
    <polygon points="190,0 570,0 570,205 190,150" fill="url(#housePhoto)" role="img" aria-label="Photo of a grey single-storey house with a new roof and garage"/>
    <polygon points="190,442 190,420 570,325 570,345 260,442" fill="#0d0d0d"/>
    <polygon points="260,442 570,345 570,442" fill="#bdbdbd"/>
    <line x1="380" y1="0" x2="380" y2="442" stroke="#000" stroke-opacity=".08"/>
    <polygon points="252,320 296,345 296,395 252,420 208,395 208,345" fill="#fff"/>
    <polygon points="252,327 290,349 290,391 252,413 214,391 214,349" fill="url(#hexPhoto)" role="img" aria-label="Photo of a roof top with new dark shingles"/>
  </svg>

  <div class="heading-strip" style="left:10px;top:30px;width:170px">INFORMATION FOR HOMEOWNERS</div>
  <div class="block body-copy body-copy--light" style="left:12px;top:56px;width:168px">
    <p>Lorem Ipsum is simply dummy text of the printing and typesetting industry. Lorem Ipsum has been the industry's standard dummy text ever since the 1500s, when an unknown printer took a galley of type and scrambled it to make a type specimen book. It has survived not only five centuries, but also the leap into electronic typesetting, remaining essentially unchanged.</p>
    <p>It was popularised in the 1960s with the release of Letraset sheets containing Lorem Ipsum passages, and more recently with desktop publishing software like Aldus PageMaker including versions of Lorem Ipsum.</p>
    <p>Contrary to popular belief, Lorem Ipsum is not simply random text. It has roots in a piece of classical Latin literature from 45 BC, making it over 2000 years old. Lorem Ipsum comes from sections 1.10.32 and 1.10.33 of "de Finibus Bonorum et Malorum" (The Extremes of Good and Evil) by Cicero, written in 45 BC.</p>
  </div>

  <div class="block" style="left:200px;top:206px;width:172px">
    <div class="heading-plain">INFORMATION FOR BUSINESS</div>
    <div class="body-copy body-copy--dark">
      <p>Contrary to popular belief, Lorem Ipsum is not simply random text. It has roots in a piece of classical Latin literature from 45 BC, making it over 2000 years old. Lorem Ipsum comes from sections 1.10.32 and 1.10.33 of "de Finibus Bonorum et Malorum" (The Extremes of Good and Evil) by Cicero, written in 45 BC. Lorem Ipsum is simply dummy text of the printing and typesetting industry.</p>
    </div>
  </div>

  <div class="block brand-name brand-name--dark" style="left:392px;top:240px;width:166px;font-size:11px">
    <span class="brand-mark" style="width:8px;height:8px"></span>Northbeam<br>Shingle &amp; Gutter<br>Works, LLC
  </div>
  <div class="block" style="left:400px;top:352px;width:160px;text-align:center">
    <span class="pill" style="font-size:10.5px;padding:2px 10px">Contact Information</span>
    <ul class="contact-list" style="margin:6px 0 0 30px">
      <li><svg viewBox="0 0 10 10"><path d="M2 1l2 2-1 1.5a6 6 0 0 0 2.5 2.5L7 6l2 2-1.5 1.5C4 9 1 6 .5 2.5z" fill="#0d0d0d"/></svg>xxx-xxxx-xxx</li>
      <li><svg viewBox="0 0 10 10"><rect x=".5" y="2" width="9" height="6" fill="none" stroke="#0d0d0d"/><path d="M.5 2l4.5 3.5L9.5 2" fill="none" stroke="#0d0d0d"/></svg>your@emailid.com</li>
    </ul>
  </div>
</section>

<section class="sheet sheet--outside" aria-label="Brochure outside spread">
  <svg class="art" viewBox="0 0 570 442">
    <defs>
      <linearGradient id="outGrey" x1="0" y1="0" x2="0" y2="1">
        <stop offset="0" stop-color="#f7f7f7"/><stop offset="1" stop-color="#bcbcbc"/>
      </linearGradient>
      <linearGradient id="yardPhoto" x1="0" y1="0" x2="0" y2="1">
        <stop offset="0" stop-color="#a9b3b8"/><stop offset=".5" stop-color="#8a8d8e"/><stop offset="1" stop-color="#5e7a45"/>
      </linearGradient>
      <linearGradient id="roofTop" x1="0" y1="0" x2="0" y2="1">
        <stop offset="0" stop-color="#9a9a9a"/><stop offset="1" stop-color="#dcdcdc"/>
      </linearGradient>
      <linearGradient id="trailerPhoto" x1="0" y1="0" x2="0" y2="1">
        <stop offset="0" stop-color="#c9c9c9"/><stop offset=".4" stop-color="#222"/><stop offset="1" stop-color="#3a3a3a"/>
      </linearGradient>
      <linearGradient id="coverPhoto" x1="0" y1="0" x2="0" y2="1">
        <stop offset="0" stop-color="#c4ccd0"/><stop offset=".55" stop-color="#7b8180"/><stop offset="1" stop-color="#5d7b45"/>
      </linearGradient>
    </defs>
    <rect x="0" y="0" width="190" height="442" fill="#0d0d0d"/>
    <polygon points="0,275 190,300 190,442 0,442" fill="url(#yardPhoto)" role="img" aria-label="Photo of a house side and yard during roof work"/>
    <polygon points="0,262 190,287 190,300 0,275" fill="#9d9d9d"/>
    <rect x="190" y="0" width="190" height="442" fill="url(#outGrey)"/>
    <rect x="190" y="0" width="190" height="62" fill="url(#roofTop)" role="img" aria-label="Photo of a freshly shingled roof surface"/>
    <polygon points="190,345 380,320 380,442 190,442" fill="url(#trailerPhoto)" role="img" aria-label="Photo of the company work trailer with roofing ladders"/>
    <rect x="380" y="0" width="190" height="442" fill="#0d0d0d"/>
    <polygon points="380,95 570,125 570,150 380,130" fill="#a0a0a0"/>
    <polygon points="380,130 570,150 570,310 380,290" fill="url(#coverPhoto)" role="img" aria-label="Photo of a grey house with red door and new roof"/>
    <polygon points="380,290 470,300 570,355 570,310" fill="#9d9d9d"/>
    <polygon points="380,372 570,412 570,440 380,400" fill="#ffffff"/>
    <line x1="190" y1="0" x2="190" y2="442" stroke="#000" stroke-opacity=".1"/>
    <line x1="380" y1="0" x2="380" y2="442" stroke="#000" stroke-opacity=".1"/>
  </svg>

  <div class="heading-strip" style="left:14px;top:14px;width:162px;text-align:center;font-size:10px">WHAT IS LOREM IPSUM?</div>
  <div class="block body-copy body-copy--light" style="left:14px;top:40px;width:164px">
    <p>Lorem Ipsum is simply dummy text of the printing and typesetting industry. Lorem Ipsum has been the industry's standard dummy text ever since the 1500s, when an unknown printer took a galley of type and scrambled it to make a type specimen book. It has survived not only five centuries, but also the leap into electronic typesetting, remaining essentially unchanged.</p>
    <p>It was popularised in the 1960s with the release of Letraset sheets containing Lorem Ipsum passages, and more recently with desktop publishing software like Aldus PageMaker including versions of Lorem Ipsum.</p>
    <p>Contrary to popular belief, Lorem Ipsum is not simply random text. It has roots in a piece of classical Latin literature from 45 BC, making it over 2000 years old. Lorem Ipsum comes from sections 1.10.32 and 1.10.33 of "de Finibus Bonorum et Malorum" (The Extremes of Good and Evil) by Cicero, written in 45 BC.</p>
  </div>

  <div class="block" style="left:196px;top:72px;width:178px;text-align:center">
    <div style="font-size:7px;color:var(--ink);margin-bottom:5px">Northbeam Shingle &amp; Gutter Works, LLC</div>
    <span class="pill" style="font-size:10.5px;padding:2px 12px">Contact Information</span>
    <ul class="contact-list" style="margin:6px 0 0 40px">
      <li><svg viewBox="0 0 10 10"><path d="M2 1l2 2-1 1.5a6 6 0 0 0 2.5 2.5L7 6l2 2-1.5 1.5C4 9 1 6 .5 2.5z" fill="#0d0d0d"/></svg>xxx-xxxx-xxx</li>
      <li><svg viewBox="0 0 10 10"><rect x=".5" y="2" width="9" height="6" fill="none" stroke="#0d0d0d"/><path d="M.5 2l4.5 3.5L9.5 2" fill="none" stroke="#0d0d0d"/></svg>your@emailid.com</li>
      <li><svg viewBox="0 0 10 10"><path d="M5 .5a3.3 3.3 0 0 0-3.3 3.3C1.7 6.3 5 9.5 5 9.5s3.3-3.2 3.3-5.7A3.3 3.3 0 0 0 5 .5z" fill="#0d0d0d"/><circle cx="5" cy="3.8" r="1.2" fill="#fff"/></svg>your address here</li>
    </ul>
  </div>
  <div class="block brand-name brand-name--dark" style="left:205px;top:200px;width:160px;font-size:10px">
    <span class="brand-mark" style="width:7px;height:7px"></span>Northbeam<br>Shingle &amp; Gutter<br>Works, LLC
  </div>
  <div class="block" style="left:196px;top:276px;width:178px;text-align:center">
    <span class="pill" style="font-family:'Jost',sans-serif;font-size:8.5px;padding:3px 14px">www.northbeamroofs.com</span>
  </div>

  <div class="block brand-name brand-name--light" style="left:390px;top:30px;width:170px;font-size:11px">
    <span class="brand-mark" style="width:8px;height:8px"></span>Northbeam<br>Shingle &amp; Gutter<br>Works, LLC
  </div>
  <div class="block cover-title" style="left:400px;top:316px;width:165px;font-size:14px">
    <strong style="font-size:16px">GIVING</strong><br>Peace of Mind<br>to Alastkans
  </div>
  <div class="block cover-tagline" style="left:385px;top:399px;width:180px;font-size:9.5px">One Roof at a Time</div>
</section>

</body>
</html>
```